Buch-/E-Book-Cover für Kinderbuch zum spielerischen Umgang zwischen Kind und Hund
Zielgruppe
Die Zielgruppe sind Kinder die lernen möchten mit Ihrem Hund besser zu spielen, verstehen und erziehen. Es ist ein Kinderbuch und das Buch soll dementsprechend 'kinderlicher' gestaltet sein.
Ich habe kein eigenes Konzept für das Cover mir derzeitig überlegt und ich werde die erstellten Cover bei meiner Zielgruppe testen und danach den Gewinner küren.
In diesem Buch handelt sich um ein Sachbuch zum Thema Hundeerziehung für Kinder. Ich möchte Ihnen die Inhaltsangabe, Vorwort und Buchrückseite mitteilen. Das Buch werde ich auf Lesefuchs.de veröffentlichen. Außerdem möchte ich Ihnen die 2 größten Konkurrenten vorstellen.
Das Vorwort:
Vorwort
Der Hund ist für das Kind mehr als nur ein vierbeiniger Hausgenosse mit Kuschelfaktor, er ist ein echter Partner zum Spielen und Lernen. Mit den passenden Ideen gestaltet sich der Alltag mit dem Tier richtig spannend. Sowohl Kind als auch Hund entwickeln sich Schritt für Schritt weiter und wachsen immer mehr zusammen. Für Jungen und Mädchen gibt es vielfältige Möglichkeiten, sich mit ihrem Vierbeiner zu beschäftigen. Kreative Rollenspiele gehören ebenso dazu wie das Lernen von Kunststücken, das Training von Intelligenz und Geschicklichkeit und das Basteln schöner Spielsachen. Lassen Sie sich von diesem Buch inspirieren und von den Fähigkeiten Ihrer Kinder und Hunde überraschen!
Gliederung:
Einleitung und Grundlegendes
1. Warum spielen Hunde und Kinder?
Gemeinsamkeiten zwischen Kind und Welpe
Die Vorteile einer engen Hund-Kind-Beziehung
Kind und Hund – das absolute Dream-Team?
Welcher Hund passt zum Kind?
Voraussetzungen für sicheres Spielen
2. Kreative Spiele
Kreative Beschäftigung mit dem Hund – darf das sein?
Rollenspiele mit Hunden
Das richtige Alter für Rollenspiele
Beispiele für typische Rollenspiele im Kindesalter
Tierische Rollenspiele – vom Kind zum Hund
Eigene Kommandos erfi..
Aufgabenstellung
Der Titel vom Buch lautet: Lauf zu uns! Wie Knirpse ihren Vierbeiner deuten, anleiten und mit ihm toben dürfen.
Das sind die 2 größten Konkurrenten https://www.lesefuchs-shop.de/Pfoten-Fibel-fuer-Kleine/p/8812345670
https://www.lesefuchs-shop.de/Bello-und-ich-Welpenwelt/p/8812345671
Das sind Cover auf dem Englisch sprachigen Markt die ich sehr gut finde
1. https://www.pageharbor-books.com/item/7720034511?search=puppy+games+for+children
2. https://www.pageharbor-books.com/item/7720034512?ref=similar

```html
<!DOCTYPE html>
<html lang="de">
<head>
<meta charset="utf-8">
<title>Lauf zu uns! – Buchdoppelseite</title>
<link rel="stylesheet" href="https://fonts.googleapis.com/css2?family=Chewy&family=Patrick+Hand&family=Permanent+Marker&display=swap">
<style>
  :root {
    --bg: #dcdbdb;
    --blue: #2c90c8;
    --blue-deep: #1f6f9f;
    --spine: #174a6e;
    --white: #ffffff;
    --paper: #e4e4e4;
    --paper-dark: #cfcfcf;
    --text-blue: #2a8dc5;
  }
  * { margin: 0; padding: 0; box-sizing: border-box; }
  html, body { width: 1200px; height: 800px; overflow: hidden; background: var(--bg); }

  .spread {
    position: absolute;
    left: 115px; top: 50px;
    width: 970px; height: 700px;
    display: flex;
  }

  /* Linke Seite: Vorwort */
  .page-foreword {
    position: relative;
    width: 456px; height: 100%;
    background: var(--blue);
    overflow: hidden;
  }
  .page-foreword .stripes { position: absolute; inset: 0; }
  .foreword-title {
    position: absolute;
    top: 30px; left: 0; width: 100%;
    text-align: center;
    font-family: "Chewy", system-ui, sans-serif;
    font-size: 60px;
    color: var(--white);
    letter-spacing: 1px;
  }
  .foreword-box {
    position: absolute;
    left: 47px; top: 130px;
    width: 370px; height: 524px;
    background: linear-gradient(160deg, #ececec 0%, var(--paper) 45%, var(--paper-dark) 100%);
    padding: 18px 24px;
    display: flex; align-items: flex-start; justify-content: center;
  }
  .foreword-text {
    font-family: "Patrick Hand", system-ui, sans-serif;
    font-weight: 700;
    font-size: 18.3px;
    line-height: 25px;
    color: var(--text-blue);
    text-align: center;
  }

  /* Buchrücken */
  .spine {
    width: 24px; height: 100%;
    background: linear-gradient(90deg, var(--spine), #1d5a84 60%, var(--spine));
  }

  /* Rechte Seite: Cover */
  .page-cover {
    position: relative;
    width: 490px; height: 100%;
    background: var(--white);
    overflow: hidden;
  }
  .cover-title {
    position: absolute;
    top: 8px; left: 0; width: 100%;
    text-align: center;
    font-family: "Chewy", system-ui, sans-serif;
    font-size: 84px;
    line-height: 78px;
    color: var(--blue);
  }
  .cover-title .line-two { display: block; font-size: 88px; }
  .subtitle-band {
    position: absolute;
    left: 0; top: 174px;
    width: 100%; height: 110px;
  }
  .subtitle-band svg { position: absolute; inset: 0; }
  .cover-subtitle {
    position: relative;
    padding-top: 16px;
    text-align: center;
    font-family: "Permanent Marker", system-ui, sans-serif;
    font-size: 21px;
    line-height: 29px;
    color: var(--white);
    text-transform: uppercase;
    letter-spacing: 1px;
  }
  .cover-photo {
    position: absolute;
    left: 0; top: 284px;
    width: 100%; height: 416px;
    background:
      radial-gradient(ellipse at 70% 70%, #3a5f8f 0%, rgba(58,95,143,0) 55%),
      linear-gradient(180deg, #b9bcbf 0%, #6d7880 45%, #3e4a55 100%);
  }
</style>
</head>
<body>
  <main class="spread">
    <section class="page-foreword">
      <svg class="stripes" width="456" height="700" viewBox="0 0 456 700" aria-hidden="true">
        <g fill="#ffffff">
          <polygon points="0,28 22,26 20,34 0,35"/>
          <polygon points="410,48 456,46 456,58 420,60 404,56"/>
          <polygon points="0,105 150,98 200,108 120,115 0,112"/>
          <polygon points="0,168 40,166 42,176 0,178"/>
          <polygon points="424,172 456,170 456,184 428,186"/>
          <polygon points="0,230 44,228 46,238 0,240"/>
          <polygon points="420,296 456,294 456,308 424,310"/>
          <polygon points="0,356 46,354 44,366 0,368"/>
          <polygon points="418,388 456,384 456,400 420,402"/>
          <polygon points="0,462 46,458 46,472 0,474"/>
          <polygon points="420,470 456,470 456,482 422,484"/>
          <polygon points="0,548 46,544 46,558 0,560"/>
          <polygon points="420,530 456,528 456,546 424,548"/>
          <polygon points="0,620 46,616 46,630 0,632"/>
          <polygon points="420,612 456,610 456,624 422,626"/>
          <polygon points="0,690 456,682 456,700 0,700"/>
        </g>
      </svg>
      <h2 class="foreword-title">Vorwort</h2>
      <div class="foreword-box">
        <p class="foreword-text">Der Hund ist für das Kind mehr als nur ein vierbeiniger Hausgenosse mit Kuschelfaktor, er ist ein echter Partner zum Spielen und Lernen. Mit den passenden Ideen gestaltet sich der Alltag mit dem Tier richtig spannend. Sowohl Kind als auch Hund entwickeln sich Schritt für Schritt weiter und wachsen immer mehr zusammen. Für Jungen und Mädchen gibt es vielfältige Möglichkeiten, sich mit ihrem Vierbeiner zu beschäftigen. Kreative Rollenspiele gehören ebenso dazu wie das Lernen von Kunststücken, das Training von Intelligenz und Geschicklichkeit und das Basteln schöner Spielsachen. Lassen Sie sich von diesem Buch inspirieren und von den Fähigkeiten Ihrer Kinder und Hunde überraschen!</p>
      </div>
    </section>

    <div class="spine" aria-hidden="true"></div>

    <section class="page-cover">
      <h1 class="cover-title">Lauf<span class="line-two">zu uns!</span></h1>
      <div class="subtitle-band">
        <svg width="490" height="110" viewBox="0 0 490 110" preserveAspectRatio="none" aria-hidden="true">
          <polygon fill="#2c90c8" points="0,12 490,0 490,104 0,110"/>
          <polygon fill="#ffffff" points="0,36 64,34 66,40 0,42"/>
          <polygon fill="#ffffff" points="20,78 70,76 72,82 22,84"/>
        </svg>
        <p class="cover-subtitle">Wie Knirpse ihren Vierbeiner<br>deuten, anleiten und mit ihm<br>toben dürfen</p>
      </div>
      <div class="cover-photo" role="img" aria-label="Foto: Ein Junge sitzt auf einer Treppe und zeigt seinem Hund einen bunten Spielball"></div>
    </section>
  </main>
</body>
</html>
```